Business Card Design (NEW FILES)

ATTENTION: New vector files are available. Please update your design to reflect/use the new (better resolution) logo images.

Seeking a unique and professional business card design for a commercial drone photography/videography business. The layout should feature
the logo (attached) and include the following information:
Pete Varner
978-552-6170
www.skylarkvisuals.example
NVR Certified Remote Pilot

Pete Varner

```html
<!DOCTYPE html>
<html lang="en">
<head>
<meta charset="utf-8">
<title>Skylark Visuals – Business Card</title>
<link rel="stylesheet" href="https://fonts.googleapis.com/css2?family=Open+Sans:wght@400;600;700&display=swap">
<style>
  :root {
    --backdrop: #232323;
    --card: #ffffff;
    --navy: #1c1f4a;
    --orange: #ee8d52;
  }
  * { margin: 0; padding: 0; box-sizing: border-box; }
  html, body {
    width: 1200px; height: 780px; overflow: hidden;
    background: var(--backdrop);
    font-family: "Open Sans", Arial, sans-serif;
    color: var(--navy);
  }
  .card {
    position: absolute;
    left: 297px; width: 607px; height: 347px;
    background: var(--card);
    border-radius: 26px;
    border-left: 4px solid var(--orange);
    border-bottom: 4px solid var(--orange);
  }
  .card--front { top: 25px; }
  .card--back  { top: 407px; }

  .brand {
    position: absolute; left: 0; right: 0; top: 148px;
    display: flex; align-items: center; justify-content: center; gap: 14px;
    font-weight: 600; font-size: 44px; letter-spacing: 1px; color: var(--navy);
  }
  .brand__dot {
    width: 34px; height: 34px; border-radius: 50%;
    background: var(--orange);
  }
  .services {
    position: absolute; left: 0; right: 0; top: 294px;
    text-align: center; font-size: 16px; font-weight: 600;
  }

  .person {
    position: absolute; right: 352px; top: 142px; text-align: right;
  }
  .person__name { font-size: 30px; font-weight: 700; line-height: 1.1; }
  .person__first { color: var(--orange); }
  .person__role { font-size: 16px; font-weight: 600; margin-top: 2px; }

  .divider {
    position: absolute; left: 301px; top: 120px;
    width: 1px; height: 100px; background: var(--orange);
  }
  .contact {
    position: absolute; left: 353px; top: 152px; list-style: none;
    font-size: 16px; font-weight: 600;
  }
  .contact li { display: flex; align-items: center; gap: 9px; height: 21px; }
  .contact svg { width: 13px; height: 13px; flex: none; }

  .credential {
    position: absolute; left: 0; right: 0; top: 290px;
    text-align: center; font-size: 16px; font-weight: 600;
  }
</style>
</head>
<body>

<section class="card card--front">
  <div class="brand"><span class="brand__dot"></span>Skylark Visuals</div>
  <p class="services">Drone Photography and Videography Services</p>
</section>

<section class="card card--back">
  <div class="person">
    <p class="person__name"><span class="person__first">Pete</span> Varner</p>
    <p class="person__role">Owner</p>
  </div>
  <span class="divider"></span>
  <ul class="contact">
    <li>
      <svg viewBox="0 0 24 24" aria-hidden="true"><path fill="#ee8d52" d="M6.6 10.8a15.1 15.1 0 0 0 6.6 6.6l2.2-2.2c.3-.3.7-.4 1-.2 1.1.4 2.3.6 3.6.6.6 0 1 .4 1 1V20c0 .6-.4 1-1 1A17 17 0 0 1 3 4c0-.6.4-1 1-1h3.5c.6 0 1 .4 1 1 0 1.3.2 2.5.6 3.6.1.3 0 .7-.2 1z"/></svg>
      978-552-6170
    </li>
    <li>
      <svg viewBox="0 0 24 24" aria-hidden="true"><circle cx="12" cy="12" r="10" fill="none" stroke="#ee8d52" stroke-width="2.4"/><path fill="none" stroke="#ee8d52" stroke-width="2" d="M2 12h20M12 2c3 3 3 17 0 20M12 2c-3 3-3 17 0 20"/></svg>
      www.skylarkvisuals.example
    </li>
  </ul>
  <p class="credential">Fully Insured - NVR Certified Remote Pilot</p>
</section>

</body>
</html>
```